Website page design

Hi, I need to improve the look of my homepage and the final offer page of my website. www.Pebble7dock.com We have an orvex buyback program where we purchase used orvex products from consumers nationwide. If you would go click through a sample offer on the site, you will the last view final offer page where we give you a cash offer for you site. I would like to keep the red and white colors since my logo is red and white. Please pay attention to the information shown on the homepage now, it is important for me to show the visitors this information on the home page. I would also love to give the users a friendly and inviting look when clicking on the options of orvex products on the home page.

Target Market(s)

Orvex electronics consumers

Number of Pages Required

2 page

Requirements
Nice to have
• On the final offer page, i would love for the offer to give an exciting look for the pebble 7 dock offer, and a boring look for the orvex buy back offer. At the final offer page you will my websites offer ( Your Pebble7dock Offer ) vs ( Orvex buyback program offer ) which is my competitor.

```html
<!DOCTYPE html>
<html lang="en">
<head>
<meta charset="utf-8">
<title>Pebble7dock — Sell Your Orvex Device</title>
<link rel="stylesheet" href="https://fonts.googleapis.com/css2?family=Raleway:wght@700;800;900&family=Lato:wght@400;700&family=Poppins:wght@400;500&display=swap">
<style>
:root{
  --red:#c4000f;
  --red-dark:#9c000b;
  --white:#ffffff;
  --ink:#1a1a1a;
  --grey-hero-a:#f1f1f1;
  --grey-hero-b:#d2d2d2;
  --panel-grey:rgba(150,150,150,.75);
  --footer:#050505;
}
*{box-sizing:border-box;margin:0;padding:0}
html,body{width:1200px;height:3415px;overflow:hidden;background:var(--white)}
body{position:relative;font-family:"Lato",sans-serif;color:var(--ink)}

/* header */
.site-header{position:absolute;left:0;top:0;width:1200px;height:118px;background:var(--red)}
.brand{position:absolute;display:flex;align-items:center;gap:8px}
.brand-mark{width:85px;height:74px;background:var(--white);display:flex;align-items:center;justify-content:center}
.brand-mark span{display:block;width:52px;height:46px;background:var(--red)}
.brand-name{font-family:"Raleway",sans-serif;font-weight:700;font-size:21px;color:var(--white);letter-spacing:.3px}
.main-nav{position:absolute;right:60px;top:48px;display:flex;gap:22px}
.main-nav a{display:flex;align-items:center;gap:5px;color:var(--white);text-decoration:none;font-family:"Lato",sans-serif;font-weight:700;font-size:17px}
.main-nav svg{width:15px;height:15px;fill:var(--white)}

/* hero */
.hero{position:absolute;left:0;top:118px;width:1200px;height:654px;background:radial-gradient(ellipse at 55% 50%,var(--grey-hero-a),var(--grey-hero-b))}
.hero-art{position:absolute;left:318px;top:136px;width:854px;height:410px;background:linear-gradient(120deg,#c9c9c9,#6b3b78 45%,#b34fa6 60%,#e7e7e7);opacity:.85;border-radius:6px}
.hero-title{position:absolute;left:0;top:107px;width:308px;height:232px;background:var(--panel-grey);box-shadow:8px 8px 0 rgba(140,140,140,.6);text-align:center;font-family:"Raleway",sans-serif;font-weight:800;line-height:1}
.hero-title .t1{display:block;color:var(--red);font-size:53px;margin-top:14px}
.hero-title .t2{display:block;color:var(--white);font-size:80px;margin-top:2px}
.hero-title .t3{display:block;color:var(--red);font-size:53px;margin-top:2px}

/* section heads */
.section-title{position:absolute;font-family:"Raleway",sans-serif;font-weight:900;font-size:37px;color:var(--red);text-shadow:2px 3px 3px rgba(0,0,0,.35);letter-spacing:.5px}
.title-rule{position:absolute;width:120px;height:12px}
.title-rule::before{content:"";position:absolute;left:0;top:4px;width:114px;height:3px;border-top:1px solid #999;border-bottom:1px solid #999}
.title-rule::after{content:"";position:absolute;right:0;top:0;width:12px;height:12px;border-radius:50%;background:var(--red)}

/* about */
.about-copy{position:absolute;left:68px;top:1000px;width:422px;font-size:15.5px;line-height:25px}
.store-label{position:absolute;left:62px;top:1136px;font-family:"Raleway",sans-serif;font-weight:800;font-size:27px}
.partner{position:absolute;display:flex;align-items:center;gap:8px;font-family:"Lato",sans-serif;font-weight:700;font-size:30px;color:var(--ink)}
.partner i{display:block;width:16px;height:16px;background:var(--red)}
.about-art{position:absolute;left:590px;top:937px;width:544px;height:316px;background:linear-gradient(180deg,#1b2a52,#3b5480 55%,#a9b3c4);border-radius:14px 14px 4px 4px}
.slider-dots{position:absolute;left:820px;top:1289px;display:flex;gap:14px}
.slider-dots span{width:14px;height:14px;border-radius:50%;background:#111}
.slider-dots span.active{background:var(--red)}

/* devices */
.devices{position:absolute;left:0;top:1416px;width:1200px;height:905px;background:linear-gradient(160deg,#3a2a22,#4a4a4d 40%,#3d3d40 70%,#5a3d28)}
.devices-title{position:absolute;left:0;top:88px;width:1200px;text-align:center;font-family:"Raleway",sans-serif;font-weight:900;font-size:37px;color:var(--white);text-shadow:2px 3px 3px rgba(0,0,0,.5)}
.devices-rule{position:absolute;left:540px;top:154px;width:115px;height:2px;background:var(--white)}
.device-card{position:absolute;width:391px;height:233px;background:var(--white);box-shadow:8px 8px 0 #111;text-align:left}
.device-badge{position:absolute;left:50%;top:-51px;width:102px;height:102px;margin-left:-51px;background:var(--red);transform:rotate(45deg)}
.device-thumb{position:absolute;left:50%;top:-33px;width:36px;height:54px;margin-left:-18px;background:linear-gradient(180deg,#f4f4f4,#c8c8c8);border-radius:5px}
.device-thumb.wide{width:62px;height:40px;margin-left:-31px;top:-20px;border-radius:3px;background:linear-gradient(180deg,#c07aa0,#e9e9e9)}
.device-name{position:absolute;left:0;top:90px;width:100%;text-align:center;font-family:"Raleway",sans-serif;font-weight:800;font-size:24px;color:var(--red)}
.device-copy{position:absolute;left:25px;top:128px;width:345px;font-size:14px;line-height:25px}

/* how it works */
.step{position:absolute;width:340px;text-align:center}
.step-icon{width:138px;height:138px;margin:0 auto;border-radius:50%;background:var(--red);box-shadow:inset -14px -14px 0 rgba(0,0,0,.12);display:flex;align-items:center;justify-content:center}
.step-icon svg{width:74px;height:74px}
.step h3{margin-top:23px;font-family:"Poppins",sans-serif;font-weight:400;font-size:28px;color:var(--red)}
.step p{margin-top:6px;font-family:"Poppins",sans-serif;font-size:16px;color:var(--ink)}

/* feed */
.feed{position:absolute;left:0;top:2834px;width:1200px;height:196px;display:flex}
.feed-label{width:232px;height:196px;background:var(--red);color:var(--white);text-align:center;padding-top:26px}
.feed-dot{display:block;width:36px;height:36px;margin:2px auto 0;border:3px solid var(--white);border-radius:50%}
.feed-label p{font-family:"Lato",sans-serif;font-size:28px;margin-top:12px}
.feed-label hr{width:54px;margin:12px auto 0;border:0;border-top:2px solid var(--white)}
.feed-tile{flex:1;height:196px}
.feed-tile.desk{background:linear-gradient(180deg,#2b2b2b,#6b5e54 55%,#d9d2c8)}
.feed-tile.lap{background:linear-gradient(180deg,#eae6de,#c9b896 60%,#8a6f4b)}

/* footer */
.site-footer{position:absolute;left:0;top:3030px;width:1200px;height:385px;background:var(--footer);color:var(--white)}
.site-footer .brand{left:478px;top:58px}
.site-footer .brand-mark{width:86px;height:76px}
.social{position:absolute;left:0;top:163px;width:1200px;display:flex;justify-content:center;gap:36px}
.social a{display:flex;align-items:center;gap:6px;color:var(--white);text-decoration:none;font-family:"Lato",sans-serif;font-weight:700;font-size:18px}
.social a i{display:block;width:20px;height:20px;border-radius:50%;background:var(--white)}
.footer-nav{position:absolute;left:348px;top:247px;display:flex;gap:47px}
.footer-nav a{color:var(--white);text-decoration:none;font-family:"Lato",sans-serif;font-weight:700;font-size:19px}
.copyright{position:absolute;left:0;top:347px;width:1200px;text-align:center;font-size:12px;font-weight:700}
</style>
</head>
<body>

<header class="site-header">
  <div class="brand" style="left:61px;top:21px">
    <div class="brand-mark"><span></span></div>
    <div class="brand-name">PEBBLE7DOCK</div>
  </div>
  <nav class="main-nav">
    <a href="#"><span>$</span>SELL</a>
    <a href="#"><svg viewBox="0 0 16 16"><circle cx="8" cy="8" r="7"/></svg>TRACK</a>
    <a href="#"><svg viewBox="0 0 16 16"><path d="M2 14l1-4 8-8 3 3-8 8z"/></svg>JOIN</a>
    <a href="#"><svg viewBox="0 0 16 16"><circle cx="8" cy="4.5" r="3.5"/><path d="M1 16c0-5 3-7 7-7s7 2 7 7z"/></svg>LOGIN</a>
  </nav>
</header>

<section class="hero">
  <div class="hero-art" role="img" aria-label="Orvex desktop, laptop, tablet and phone grouped together"></div>
  <h1 class="hero-title"><span class="t1">PEBBLE</span><span class="t2">7</span><span class="t3">DOCK</span></h1>
</section>

<section class="about">
  <h2 class="section-title" style="left:64px;top:878px">ABOUT US</h2>
  <div class="title-rule" style="left:33px;top:939px"></div>
  <p class="about-copy">Lorem Ipsum is simply dummy text of the printing and typesetting industry. Lorem Ipsum has been the industry's standard dummy text ever since the 1500s, when an unknown printer took a galley of type and scrambled it to make a type</p>
  <h3 class="store-label">STORE</h3>
  <div class="partner" style="left:77px;top:1197px"><i></i>Marketoria</div>
  <div class="partner" style="left:300px;top:1197px"><i></i>Bidloop</div>
  <div class="partner" style="left:77px;top:1273px"><i></i>Ratewise</div>
  <div class="partner" style="left:300px;top:1273px"><i></i>Marketoria</div>
  <div class="about-art" role="img" aria-label="Orvex laptop showing a desert dune wallpaper"></div>
  <div class="slider-dots"><span class="active"></span><span></span><span></span></div>
</section>

<section class="devices" role="region" aria-label="Select your device">
  <h2 class="devices-title">SELECT YOUR DEVICE TO RECEIVE AN INSTANT QUOTE</h2>
  <div class="devices-rule"></div>

  <article class="device-card" style="left:126px;top:271px">
    <div class="device-badge"></div>
    <div class="device-thumb" role="img" aria-label="Vexphone"></div>
    <h3 class="device-name">Vexphone</h3>
    <p class="device-copy">Lorem Ipsum is simply dummy text of the printing and typesetting industry. Lorem Ipsum has been the industry's</p>
  </article>
  <article class="device-card" style="left:680px;top:271px">
    <div class="device-badge"></div>
    <div class="device-thumb" style="width:40px;height:52px;margin-left:-20px" role="img" aria-label="Vexpad"></div>
    <h3 class="device-name">Vexpad</h3>
    <p class="device-copy">Lorem Ipsum is simply dummy text of the printing and typesetting industry. Lorem Ipsum has been the industry's</p>
  </article>
  <article class="device-card" style="left:126px;top:622px">
    <div class="device-badge"></div>
    <div class="device-thumb wide" role="img" aria-label="Vexbook"></div>
    <h3 class="device-name">Vexbook</h3>
    <p class="device-copy">Lorem Ipsum is simply dummy text of the printing and typesetting industry. Lorem Ipsum has been the industry's</p>
  </article>
  <article class="device-card" style="left:680px;top:622px">
    <div class="device-badge"></div>
    <div class="device-thumb wide" role="img" aria-label="Vexdesk"></div>
    <h3 class="device-name">Vexdesk</h3>
    <p class="device-copy">Lorem Ipsum is simply dummy text of the printing and typesetting industry. Lorem Ipsum has been the industry's</p>
  </article>
</section>

<section class="how">
  <h2 class="section-title" style="left:62px;top:2400px">HOW IT WORKS</h2>
  <div class="title-rule" style="left:33px;top:2463px"></div>

  <div class="step" style="left:62px;top:2526px">
    <div class="step-icon"><svg viewBox="0 0 74 74"><path fill="#fff" d="M37 4l7 7 10-2 2 10 10 5-4 9 4 9-10 5-2 10-10-2-7 7-7-7-10 2-2-10-10-5 4-9-4-9 10-5 2-10 10 2z"/><text x="37" y="47" text-anchor="middle" font-family="Poppins,sans-serif" font-size="28" fill="#c4000f">%</text></svg></div>
    <h3>Get An Offer</h3>
    <p>Less than a minute</p>
  </div>
  <div class="step" style="left:431px;top:2526px">
    <div class="step-icon"><svg viewBox="0 0 74 74"><rect x="4" y="20" width="42" height="28" rx="2" fill="#fff"/><path fill="#fff" d="M48 28h12l10 10v10H48z"/><circle cx="18" cy="52" r="6" fill="#fff" stroke="#c4000f" stroke-width="3"/><circle cx="58" cy="52" r="6" fill="#fff" stroke="#c4000f" stroke-width="3"/><text x="25" y="39" text-anchor="middle" font-family="Lato,sans-serif" font-weight="700" font-size="12" fill="#c4000f">FREE</text></svg></div>
    <h3>Ship It Free.</h3>
    <p>We provide a pre-paid shipping label</p>
  </div>
  <div class="step" style="left:799px;top:2526px">
    <div class="step-icon"><svg viewBox="0 0 74 74"><g stroke="#fff" stroke-width="4" fill="none"><path d="M6 26h20M10 37h16M6 48h20"/><circle cx="40" cy="37" r="14"/><path d="M54 26h14M54 37h16M54 48h14"/></g><text x="40" y="45" text-anchor="middle" font-family="Lato,sans-serif" font-weight="700" font-size="20" fill="#fff">$</text></svg></div>
    <h3>Get Paid Fast</h3>
    <p>Paywell, check or bank transfer</p>
  </div>
</section>

<section class="feed">
  <div class="feed-label">
    <span class="feed-dot"></span>
    <p>Photofeed</p>
    <hr>
  </div>
  <div class="feed-tile desk" role="img" aria-label="Orvex desktop on a desk"></div>
  <div class="feed-tile lap" role="img" aria-label="Orvex laptop on a wooden table"></div>
  <div class="feed-tile desk" role="img" aria-label="Orvex desktop on a desk"></div>
  <div class="feed-tile lap" role="img" aria-label="Orvex laptop on a wooden table"></div>
  <div class="feed-tile desk" role="img" aria-label="Orvex desktop on a desk"></div>
</section>

<footer class="site-footer">
  <div class="brand">
    <div class="brand-mark"><span></span></div>
    <div class="brand-name">PEBBLE7DOCK</div>
  </div>
  <div class="social">
    <a href="#"><i></i>Friendsy</a>
    <a href="#"><i></i>Pixgram</a>
  </div>
  <nav class="footer-nav">
    <a href="#">Home</a><a href="#">About</a><a href="#">Sell Buy</a><a href="#">Contact</a><a href="#">FAQ</a>
  </nav>
  <p class="copyright">© 2019 — All rights reserved.</p>
</footer>

</body>
</html>
```